Brackwell Renovations needs a website.

I need a platform for clients to go and learn about what my company does, see pictures of projects, and contact me about their projects. I am a residential remodeler specializing in general contracting services for kitchens, bathrooms, basements, additions, custom interiors, and more. I have attached my logo to be incorporated.

```html
<!DOCTYPE html>
<html lang="en">
<head>
<meta charset="utf-8">
<title>Brackwell Renovations</title>
<link href="https://fonts.googleapis.com/css2?family=Krona+One&family=Roboto:wght@400;500;700&display=swap" rel="stylesheet">
<style>
:root{
  --green:#0d4a0a;
  --green-dark:#0a3a08;
  --grey:#8a8c8c;
  --grey-text:#8f9191;
  --light:#f0f0f0;
  --ink:#1a1a1a;
  --body:#555;
  --white:#fff;
  --black:#050505;
  --star:#f08a00;
}
*{box-sizing:border-box;margin:0;padding:0}
html,body{width:1200px;height:5008px;overflow:hidden}
body{position:relative;font-family:"Roboto",sans-serif;color:var(--ink);background:var(--white)}
.abs{position:absolute}
.display{font-family:"Krona One",sans-serif;text-transform:uppercase;letter-spacing:.5px}
.muted{color:var(--grey-text)}
.eyebrow{font-family:"Roboto",sans-serif;font-weight:700;font-size:18px;color:var(--green);text-transform:uppercase;display:flex;align-items:center;gap:8px}
.eyebrow .mark{width:22px;height:22px;border:2px solid currentColor;border-radius:50%}
.center{left:0;width:1200px;justify-content:center;text-align:center}
.btn{display:flex;align-items:center;justify-content:center;gap:8px;background:var(--green);color:var(--white);border-radius:30px;font-weight:700;text-transform:uppercase}
.btn .dot{width:14px;height:14px;border-radius:50%;background:var(--white);display:inline-flex;align-items:center;justify-content:center}

/* top bar */
.topbar{top:0;left:0;width:1200px;height:33px;background:var(--grey);color:var(--white);font-size:14px}
.topbar .item{top:7px;display:flex;align-items:center;gap:8px}
.topbar .ic{width:22px;height:22px;border-radius:50%;background:var(--white);display:flex;align-items:center;justify-content:center}
.social{top:5px;width:22px;height:22px;border-radius:50%;background:var(--white)}

/* header */
.header{top:33px;left:0;width:1200px;height:97px;background:var(--white)}
.brand{display:flex;align-items:center;gap:10px;font-family:"Roboto",sans-serif;font-weight:700;color:var(--ink);line-height:1}
.brand .badge{border:3px solid var(--green);border-radius:50%}
.nav{top:43px;left:449px;display:flex;gap:22px;font-size:16px;font-weight:500}
.nav .active{color:var(--green)}

/* hero */
.hero{top:130px;left:0;width:1200px;height:660px;background:linear-gradient(100deg,#2e2b28 0%,#4a4540 35%,#7d756b 60%,#b9b2a6 80%,#8f877d 100%)}
.hero .shade{position:absolute;inset:0;background:linear-gradient(90deg,rgba(0,0,0,.55),rgba(0,0,0,0) 60%)}

/* about */
.ring{left:111px;top:815px;width:470px;height:470px;border-radius:50%;border:12px solid #8f9191;border-right-color:transparent}
.about-photo{left:140px;top:845px;width:415px;height:415px;border-radius:50%;background:linear-gradient(160deg,#3f67b4 0%,#6e86b8 35%,#3d3530 60%,#b67834 80%,#2a2724 100%)}
.years{left:422px;top:1151px;width:140px;height:140px;border-radius:50%;background:var(--green);border:4px solid var(--white);color:var(--white);text-align:center;font-family:Georgia,serif;padding-top:26px}
.about-text{left:650px;top:865px;width:450px}
.about-text h2{font-size:28px;line-height:36px;margin-top:18px}
.about-text p{font-size:14px;line-height:25px;color:var(--body);margin-top:24px}
.about-text p+p{margin-top:12px}

/* services */
.services{top:1390px;left:0;width:1200px;height:652px;background:var(--light)}
.card{top:187px;width:237px;height:360px;background:var(--white);border-radius:10px;overflow:hidden;box-shadow:0 6px 18px rgba(0,0,0,.08)}
.card .photo{height:290px}
.card .label{height:70px;display:flex;align-items:center;justify-content:space-between;padding:0 14px;font-weight:700;font-size:17px;text-transform:uppercase}
.card .go{width:44px;height:44px;border-radius:50%;background:var(--green);display:flex;align-items:center;justify-content:center}
.card.active .label{background:var(--green-dark);color:var(--white)}
.card.active .go{background:var(--white)}
.arrow-btn{width:46px;height:46px;border-radius:50%;border:2px solid #555;display:flex;align-items:center;justify-content:center}

/* benefits */
.benefits{top:2042px;left:0;width:1200px;height:343px;background:var(--green);color:var(--white)}
.benefit{top:177px;width:260px;text-align:center;font-size:16px;font-weight:500}
.benefit .icon{width:78px;height:78px;border-radius:50%;background:#8f9191;margin:0 auto 22px;display:flex;align-items:center;justify-content:center}

/* gallery */
.tile{border-radius:6px}
.plus{width:46px;height:46px;border-radius:50%;background:var(--white);display:flex;align-items:center;justify-content:center}

/* testimonials */
.testimonials{top:3350px;left:0;width:1200px;height:491px;background:var(--grey)}
.quote-card{top:186px;width:407px;height:232px;background:var(--white);border-radius:24px;box-shadow:0 6px 16px rgba(0,0,0,.15)}
.quote-card .avatar{position:absolute;left:-52px;top:56px;width:116px;height:116px;border-radius:50%;background:linear-gradient(160deg,#c9cccd,#6f7377);border:4px solid var(--white)}
.quote-card .q{position:absolute;left:100px;top:14px;font-family:Georgia,serif;font-size:64px;font-weight:700;color:var(--green)}
.quote-card p{position:absolute;left:100px;top:78px;width:280px;font-size:14px;line-height:23px;color:#777}
.quote-card .name{position:absolute;left:100px;top:152px;font-weight:700;font-size:16px}
.quote-card .stars{position:absolute;left:100px;top:172px;color:var(--star);font-size:18px;letter-spacing:2px}

/* contact */
.field{height:39px;border:1px solid #ddd;border-radius:6px;font-size:13px;color:#666;display:flex;align-items:center;justify-content:space-between;padding:0 12px}

/* footer */
.footer{top:4530px;left:0;width:1200px;height:478px}
.foot-col{top:4694px;color:var(--white)}
.foot-col h4{font-size:16px;font-weight:700;margin-bottom:18px}
.foot-col li{list-style:none;font-size:13px;line-height:26px}
.foot-contact{font-size:13px;line-height:18px}
.foot-contact b{display:block;font-size:11px}
</style>
</head>
<body>

<!-- top bar -->
<div class="abs topbar">
  <div class="abs item" style="left:111px">
    <span class="ic"><svg width="12" height="12" viewBox="0 0 12 12"><path d="M1 6 11 1 8 11 6 7Z" fill="#8a8c8c"/></svg></span>info@brackwellrenovations.com
  </div>
  <div class="abs item" style="left:375px;font-weight:700">
    <span class="ic"><svg width="12" height="12" viewBox="0 0 12 12"><path d="M2 1h3l1 3-2 1a7 7 0 0 0 3 3l1-2 3 1v3c-6 0-9-3-9-9z" fill="#8a8c8c"/></svg></span>Toll Free (888) 555-BRCK
  </div>
  <div class="abs social" style="left:961px"></div>
  <div class="abs social" style="left:996px"></div>
  <div class="abs social" style="left:1031px"></div>
  <div class="abs social" style="left:1066px"></div>
</div>

<!-- header -->
<header class="abs header">
  <div class="abs brand" style="left:111px;top:16px;font-size:19px">
    <span class="badge" style="width:62px;height:62px"></span>BRACKWELL<br>RENOVATIONS
  </div>
  <nav class="abs nav" style="top:42px">
    <span class="active">Home</span><span>About</span><span>Services</span><span>Portfolio</span><span>Testimonials</span><span>Contact</span>
  </nav>
  <div class="abs btn" style="left:947px;top:29px;width:142px;height:41px;text-transform:none;font-size:16px">Get A Quote</div>
</header>

<!-- hero -->
<section class="abs hero" role="img" aria-label="Bright white kitchen with marble island and pendant lights">
  <div class="shade"></div>
</section>
<div class="abs" style="left:111px;top:244px;color:var(--white);font-weight:700;font-size:19px">BRACKWELL RENOVATIONS</div>
<h1 class="abs display" style="left:111px;top:282px;color:var(--white);font-size:41px;line-height:52px;font-weight:400">Transforming<br>Homes, Elevating<br>Lifestyles.</h1>
<div class="abs btn" style="left:111px;top:476px;width:327px;height:54px;font-size:17px">Get A Free Consultation <span class="dot"><svg width="8" height="8" viewBox="0 0 8 8"><path d="M2 1l4 3-4 3" stroke="#0d4a0a" stroke-width="1.6" fill="none"/></svg></span></div>
<svg class="abs" style="left:0;top:680px" width="1200" height="110" viewBox="0 0 1200 110">
  <path d="M0 70 C250 150 520 95 760 85 C960 78 1100 60 1200 0 L1200 110 L0 110Z" fill="#0d4a0a"/>
  <path d="M0 80 C250 150 520 112 760 100 C960 92 1100 75 1200 25 L1200 110 L0 110Z" fill="#fff"/>
</svg>

<!-- about -->
<div class="abs ring"></div>
<div class="abs about-photo" role="img" aria-label="Modern home exterior at dusk with warm lit windows"></div>
<div class="abs years"><div style="font-size:13px">Celebrating</div><div style="font-size:36px;line-height:38px">25</div><div style="font-size:17px">Years</div></div>
<div class="abs about-text">
  <div class="eyebrow"><span class="mark"></span>About Us</div>
  <h2 class="display" style="font-weight:400">Quality Craftsmanship,<br><span class="muted">Personalized Service</span></h2>
  <p>At Brackwell Renovations, we believe your home should reflect your style and needs. With years of experience in high-quality remodeling, we specialize in transforming kitchens, bathrooms, basements, and more.</p>
  <p>Our team ensures attention to detail, clear communication, and expert execution in every project.</p>
  <div class="btn" style="width:171px;height:45px;font-size:14px;margin-top:42px">Learn More <span class="dot"><svg width="8" height="8" viewBox="0 0 8 8"><path d="M2 1l4 3-4 3" stroke="#0d4a0a" stroke-width="1.6" fill="none"/></svg></span></div>
</div>

<!-- services -->
<section class="abs services">
  <div class="abs eyebrow center" style="top:68px"><span class="mark"></span>Services We Offer</div>
  <h2 class="abs display center" style="top:106px;font-size:32px;font-weight:400;width:1200px">Bringing Your <span class="muted">Vision To Life</span></h2>
  <div class="abs arrow-btn" style="left:29px;top:344px"><svg width="14" height="14" viewBox="0 0 14 14"><path d="M9 2 4 7l5 5" stroke="#555" stroke-width="1.8" fill="none"/></svg></div>
  <div class="abs arrow-btn" style="left:1123px;top:344px"><svg width="14" height="14" viewBox="0 0 14 14"><path d="M5 2l5 5-5 5" stroke="#555" stroke-width="1.8" fill="none"/></svg></div>

  <div class="abs card" style="left:107px"><div class="photo" role="img" aria-label="Kitchen with dark wood island and pendant lights" style="background:linear-gradient(160deg,#ecebe8,#b9b3aa 55%,#5b4031)"></div><div class="label">Kitchens<span class="go"><svg width="20" height="12" viewBox="0 0 20 12"><path d="M1 6h17M13 1l5 5-5 5" stroke="#fff" stroke-width="1.8" fill="none"/></svg></span></div></div>
  <div class="abs card" style="left:358px"><div class="photo" role="img" aria-label="Marble bathroom with freestanding tub" style="background:linear-gradient(160deg,#8c8780,#d9d5cf 50%,#a39d95)"></div><div class="label">Bathrooms<span class="go"><svg width="20" height="12" viewBox="0 0 20 12"><path d="M1 6h17M13 1l5 5-5 5" stroke="#fff" stroke-width="1.8" fill="none"/></svg></span></div></div>
  <div class="abs card active" style="left:607px"><div class="photo" role="img" aria-label="Finished basement with wood floors and staircase" style="background:linear-gradient(170deg,#3c3128,#6f5136 55%,#9a6b3e)"></div><div class="label">Basements<span class="go"><svg width="20" height="12" viewBox="0 0 20 12"><path d="M1 6h17M13 1l5 5-5 5" stroke="#0d4a0a" stroke-width="1.8" fill="none"/></svg></span></div></div>
  <div class="abs card" style="left:858px"><div class="photo" role="img" aria-label="Bright living room interior with rattan furniture" style="background:linear-gradient(160deg,#c7b79c,#e8e0d2 55%,#b08a5a)"></div><div class="label">Interiors<span class="go"><svg width="20" height="12" viewBox="0 0 20 12"><path d="M1 6h17M13 1l5 5-5 5" stroke="#fff" stroke-width="1.8" fill="none"/></svg></span></div></div>
</section>

<!-- benefits -->
<section class="abs benefits">
  <div class="abs eyebrow center" style="top:57px;color:var(--white)"><span class="mark"></span>Why Choose Us</div>
  <h2 class="abs display center" style="top:96px;font-size:32px;font-weight:400;width:1200px">Benefits Of Renovations</h2>
  <div class="abs benefit" style="left:74px"><div class="icon"><svg width="40" height="40" viewBox="0 0 40 40" fill="none" stroke="#fff" stroke-width="2"><circle cx="20" cy="13" r="5"/><circle cx="9" cy="17" r="4"/><circle cx="31" cy="17" r="4"/><path d="M10 34c0-7 4-11 10-11s10 4 10 11M2 32c0-5 3-8 7-8M38 32c0-5-3-8-7-8"/></svg></div>25+ Years of Experience</div>
  <div class="abs benefit" style="left:335px"><div class="icon"><svg width="40" height="40" viewBox="0 0 40 40" fill="none" stroke="#fff" stroke-width="2"><rect x="9" y="6" width="20" height="28" rx="2"/><path d="M13 13h12M13 19h12M13 25h6"/><circle cx="28" cy="28" r="5"/></svg></div>Licensed &amp; Insured</div>
  <div class="abs benefit" style="left:588px"><div class="icon"><svg width="40" height="40" viewBox="0 0 40 40" fill="none" stroke="#fff" stroke-width="2"><circle cx="20" cy="16" r="10"/><path d="M14 24l-3 12 9-5 9 5-3-12M20 11l2 4 4 .5-3 3 1 4-4-2-4 2 1-4-3-3 4-.5z"/></svg></div>Quality Craftsmanship</div>
  <div class="abs benefit" style="left:864px"><div class="icon"><svg width="40" height="40" viewBox="0 0 40 40" fill="none" stroke="#fff" stroke-width="2"><path d="M6 36V22h6v14M12 34h16l5-10h-9l1-7c0-3-4-3-4 0l-5 7"/><path d="M8 8l1 2 2 .3-1.5 1.4.4 2-1.9-1-1.9 1 .4-2L5 10.3 7 10zM20 4l1 2 2 .3-1.5 1.4.4 2-1.9-1-1.9 1 .4-2L17 6.3 19 6zM32 8l1 2 2 .3-1.5 1.4.4 2-1.9-1-1.9 1 .4-2L29 10.3 31 10z"/></svg></div>5-Star Client Satisfaction</div>
</section>

<!-- gallery -->
<div class="abs eyebrow center" style="top:2474px"><span class="mark"></span>View Our Work</div>
<h2 class="abs display center" style="top:2512px;font-size:32px;font-weight:400;width:1200px">Project <span class="muted">Gallery</span></h2>
<div class="abs tile" role="img" aria-label="White kitchen with island seating" style="left:111px;top:2593px;width:318px;height:312px;background:linear-gradient(165deg,#f2f1ee,#d2cdc4 55%,#6d4f3a)"></div>
<div class="abs tile" role="img" aria-label="Open kitchen and dining area" style="left:111px;top:2916px;width:318px;height:219px;background:linear-gradient(165deg,#d9d6d0,#8f8677 55%,#3a3632)"></div>
<div class="abs tile" role="img" aria-label="Dark basement staircase" style="left:442px;top:2593px;width:317px;height:377px;background:linear-gradient(170deg,#4a4a4a,#2a2a2a 60%,#3b3b3b)"></div>
<div class="abs plus" style="left:577px;top:2759px"><svg width="20" height="20" viewBox="0 0 20 20"><path d="M10 2v16M2 10h16" stroke="#111" stroke-width="2.5"/></svg></div>
<div class="abs tile" role="img" aria-label="Bright living room with arched windows" style="left:442px;top:2981px;width:317px;height:154px;background:linear-gradient(165deg,#eeeae3,#cdbfa7 60%,#8e7a5d)"></div>
<div class="abs tile" role="img" aria-label="Hallway with stone accent wall and wood door" style="left:771px;top:2593px;width:316px;height:222px;background:linear-gradient(120deg,#5f574f,#8d8377 45%,#b5aea4 70%,#6b4a30)"></div>
<div class="abs tile" role="img" aria-label="Bathroom with freestanding tub and round mirror" style="left:771px;top:2826px;width:316px;height:309px;background:linear-gradient(110deg,#5a3c26,#7a5538 25%,#e3e1dd 45%,#cfcac3 100%)"></div>
<div class="abs btn" style="left:506px;top:3196px;width:189px;height:46px;font-size:14px">View All Works</div>

<!-- testimonials -->
<section class="abs testimonials">
  <div class="abs eyebrow center" style="top:68px;color:var(--white)"><span class="mark"></span>Don't Just Take Our Word For It</div>
  <h2 class="abs display center" style="top:106px;font-size:32px;font-weight:400;width:1200px;color:var(--white)">Customer Testmonials</h2>
  <svg class="abs" style="left:42px;top:286px" width="24" height="30" viewBox="0 0 24 30"><path d="M18 3 6 15l12 12" stroke="#fff" stroke-width="4" fill="none"/></svg>
  <svg class="abs" style="left:1134px;top:286px" width="24" height="30" viewBox="0 0 24 30"><path d="M6 3l12 12L6 27" stroke="#fff" stroke-width="4" fill="none"/></svg>
  <div class="abs quote-card" style="left:179px">
    <div class="avatar" role="img" aria-label="Client portrait"></div>
    <div class="q">&ldquo;</div>
    <p>Sed ut perspiciatis unde omnis iste natus sit voluptatem accusantium doloremque laudantium, totam rem aperiam,</p>
    <div class="name">Jordan Avery</div>
    <div class="stars">★★★★★</div>
  </div>
  <div class="abs quote-card" style="left:667px">
    <div class="avatar" role="img" aria-label="Client portrait"></div>
    <div class="q">&ldquo;</div>
    <p>Sed ut perspiciatis unde omnis iste natus sit voluptatem accusantium doloremque laudantium, totam rem aperiam,</p>
    <div class="name">Jordan Avery</div>
    <div class="stars">★★★★★</div>
  </div>
</section>

<!-- contact -->
<div class="abs eyebrow" style="left:111px;top:3973px"><span class="mark"></span>Contact Us</div>
<h2 class="abs display" style="left:111px;top:4002px;font-size:32px;font-weight:400">Get In <span class="muted">Touch</span></h2>
<div class="abs" style="left:113px;top:4048px;font-size:14px;color:var(--body)">Fill out the form below, &amp; we'll be in touch soon!</div>
<div class="abs field" style="left:111px;top:4108px;width:218px">Name<span>&#9679;</span></div>
<div class="abs field" style="left:342px;top:4108px;width:220px">Email<span>&#9993;</span></div>
<div class="abs field" style="left:111px;top:4166px;width:218px">Phone<span>&#9742;</span></div>
<div class="abs field" style="left:342px;top:4166px;width:220px">Select Service<span>&#9662;</span></div>
<div class="abs field" style="left:111px;top:4225px;width:451px;height:101px;align-items:flex-start;padding-top:12px">Message<span>&#9998;</span></div>
<div class="abs btn" style="left:111px;top:4376px;width:194px;height:49px;font-size:14px">Submit Now</div>
<div class="abs" role="img" aria-label="Modern two-storey house at dusk" style="left:620px;top:3950px;width:467px;height:492px;border-radius:18px;background:linear-gradient(170deg,#5b6f86,#3c4b5c 50%,#2c3229 80%,#4a3324)"></div>

<!-- footer -->
<footer class="abs footer">
  <svg class="abs" style="left:0;top:0" width="1200" height="478" viewBox="0 0 1200 478">
    <path d="M0 90 C180 30 360 10 560 45 C760 80 950 60 1200 0 L1200 478 L0 478Z" fill="#0d4a0a"/>
    <path d="M0 105 C180 50 360 28 560 62 C760 96 950 80 1200 20 L1200 478 L0 478Z" fill="#050505"/>
  </svg>
</footer>
<div class="abs brand" style="left:111px;top:4765px;font-size:22px;color:var(--white);font-weight:500">
  <span class="badge" style="width:74px;height:74px"></span>BRACKWELL<br>RENOVATIONS
</div>
<div class="abs foot-col" style="left:480px"><h4>Quick Links</h4><ul><li>Home</li><li>About</li><li>Services</li><li>Portfolio</li><li>Testimonials</li><li>Contact</li></ul></div>
<div class="abs foot-col" style="left:675px"><h4>About Company</h4><ul><li>Privacy Policy</li><li>Cookie Policy</li><li>Terms &amp; Condition</li><li>Support</li><li>Site Map</li></ul></div>
<div class="abs foot-col" style="left:889px"><h4>Contact Us</h4>
  <div class="foot-contact" style="padding-left:22px"><b>Location</b>418 Harlow Ave Ridgefield,<br>WA 98642</div>
  <div class="foot-contact" style="padding-left:22px;margin-top:12px"><b>Phone</b>(555) 214-7730</div>
  <div class="foot-contact" style="padding-left:22px;margin-top:12px"><b>Email</b>info@brackwellrenovations.com</div>
</div>
<div class="abs" style="left:1133px;top:4857px;width:34px;height:34px;border-radius:50%;background:var(--green);display:flex;align-items:center;justify-content:center"><svg width="12" height="8" viewBox="0 0 12 8"><path d="M1 7l5-5 5 5" stroke="#fff" stroke-width="2" fill="none"/></svg></div>
<div class="abs" style="left:0;top:4955px;width:1200px;text-align:center;color:var(--white);font-size:14px">2025 Copyright - Brackwell Renovations | All Rights Reserved</div>

</body>
</html>
```